Cupcakes blog redesign - cartoon/illustrated style

I need to redesign my food blog muffinmeadow.net.

I really like the current blog design but I want to change Pressleaf theme to responsive and I want to refresh the look of the blog.

Blog design must be in the same style (cartoon, illustrated). The whole idea should be the same as old blog! The header illustration is some kind of garden full of cupcakes. All other elements (left sidebar menu, right sidebar widgets and footer elements) should be in that (garden of cupcakes) style.

The color sheme should be similar to old design. I really like pink, green and light blue color! The content background color must be white.
Only element that must be the same with old site is cupcakes thumbnail images (image 1 in attachment).
Feel fre to change all other elements design .

You can use illustration from http://artwellstock.net/search?utf8=%E2%9C%93&term=cupcakes. I will buy these elements later!

You can find all technical details (dimensions,elements...) in the attachment.

This is the list of sites I really like:

1. I adore header of this site - http://www.runbylake.com/
2. I adore header of this site - http://ful.marbstudio.com/
3. Big site title and overal design - http://tallowbooks.com/
4. Header - http://ful.marbstudio.com/
5. Footer style :) - http://www.orvelapin.com/
6. Color sheme - http://brisklunch.com/
7. Color sheme - http://www.mellowbake.com/
8. Color sheme - http://www.dorathysugarbox.com/

Feel free to contact me for more information.

Good luck

Here is couple illustration example I really like. Of course it should be in Muffin Meadow style:

1. http://pitchyard.net/web-design/contests/create-best-site-kids-world-267986/entries/29767275
2. http://pitchyard.net/web-design/contests/create-best-site-kids-world-267986/entries/89
3. http://layoutbrim.com/demo/wp/tot-lawn/
4. http://www.wobblecritters.com/login/forums

```html
<!DOCTYPE html>
<html lang="en">
<head>
<meta charset="utf-8">
<title>Muffin Meadow</title>
<link href="https://fonts.googleapis.com/css2?family=Lobster&family=Open+Sans:wght@400;600;700&display=swap" rel="stylesheet">
<style>
:root{
  --pink:#e9568a;
  --pink-soft:#fbd9e5;
  --pink-pale:#fdeef3;
  --sky:#bfe6f7;
  --sky-pale:#e8f7fd;
  --grass:#8cc63f;
  --grass-dark:#5e9e2a;
  --text:#6b6b6b;
  --muted:#9a9a9a;
  --line:#ececec;
  --white:#ffffff;
}
*{box-sizing:border-box;margin:0;padding:0}
html,body{width:837px;height:1200px;overflow:hidden}
body{position:relative;background:var(--white);font-family:"Open Sans",sans-serif;color:var(--text);font-size:9px;line-height:1.35}
.abs{position:absolute}

/* header */
.header-scene{left:0;top:0;width:837px;height:190px;background:linear-gradient(180deg,var(--sky-pale) 0%,var(--sky) 45%,#a6dbc0 60%,var(--grass) 75%,var(--grass-dark) 100%)}
.site-title{left:240px;top:4px;font-family:"Lobster",cursive;font-size:42px;color:var(--pink);line-height:1;white-space:nowrap}
.site-tagline{left:240px;top:52px;font-family:"Lobster",cursive;font-size:12px;color:#d2467b;white-space:nowrap}
.main-nav{left:225px;top:88px;width:380px;height:22px;background:var(--white);border-radius:11px;display:flex;align-items:center;padding:0 10px;gap:14px;box-shadow:0 1px 3px rgba(0,0,0,.15)}
.main-nav a{font-size:8.5px;font-weight:600;color:var(--pink);text-decoration:none;white-space:nowrap}
.search{margin-left:auto;width:80px;height:14px;border:1px solid var(--line);border-radius:7px;font-size:7px;color:var(--muted);padding:1px 6px}

/* left sidebar */
.cat-head{left:110px;top:200px;width:152px;height:44px;background:var(--pink-soft);border-radius:6px;font-family:"Lobster",cursive;color:var(--pink);font-size:13px;text-align:center;padding-top:5px;line-height:1.2}
.cat-list{left:110px;top:250px;width:152px;list-style:none}
.cat-list li{height:30px;display:flex;align-items:center;gap:8px;border-bottom:1px dotted var(--line);font-size:8px;color:var(--text)}
.cat-thumb{width:22px;height:22px;border-radius:50%;background:radial-gradient(circle at 50% 35%,#f7b8cf,#c98a5c)}
.cat-list li span:last-child{margin-left:auto;color:var(--pink);font-size:11px}
.ad-tall{top:418px;width:72px;height:330px;border-radius:3px}
.ad-red{left:112px;background:linear-gradient(180deg,#e8412c,#b82a1b 60%,#f3b43a)}
.ad-info{left:190px;background:linear-gradient(180deg,#2e3b4e,#e8412c 45%,#f4c23e)}
.badge-box{left:110px;top:760px;width:152px;height:120px;border:1px solid var(--line);border-radius:6px}
.badge-box h4{font-family:"Lobster",cursive;font-weight:400;color:var(--grass-dark);font-size:13px;text-align:center;margin-top:6px}
.badge-art{margin:6px auto 0;width:70px;height:76px;border-radius:8px;background:linear-gradient(180deg,var(--pink-soft),#c9e8a6)}
.code-box{left:110px;top:888px;width:152px;height:50px;border:1px solid var(--line);font-size:7px;color:var(--muted);padding:4px;font-family:monospace,monospace;overflow:hidden}

/* posts */
.post{left:275px;width:425px;height:165px;border-bottom:1px dotted #e3e3e3}
.post-thumb{position:absolute;left:3px;top:6px;width:86px;height:86px;border-radius:4px;background:radial-gradient(circle at 50% 35%,#fbe3ea,#e7a0b7 45%,#9c6a44 80%)}
.post-title{position:absolute;left:100px;top:4px;width:260px;font-family:"Lobster",cursive;font-weight:400;color:var(--pink);font-size:17px;line-height:1.15}
.post-meta{position:absolute;left:100px;top:50px;font-size:7px;color:var(--muted);line-height:1.4}
.post-excerpt{position:absolute;left:3px;top:100px;width:415px;font-size:7.5px;color:var(--text);line-height:1.4}
.read-more{position:absolute;left:3px;top:140px;background:var(--pink);color:var(--white);font-size:7px;padding:1px 7px;border-radius:2px}

.pagination{left:420px;top:1068px;display:flex;gap:3px}
.pagination span{width:13px;height:13px;border:1px solid #ddd;font-size:7px;text-align:center;line-height:11px;color:var(--text)}
.pagination span.on{background:var(--pink);color:var(--white);border-color:var(--pink)}

/* right sidebar */
.side-title{font-family:"Lobster",cursive;color:var(--pink);font-size:13px;white-space:nowrap}
.follow{left:718px;top:200px;width:112px}
.socials{display:flex;gap:4px;margin-top:4px}
.socials i{width:18px;height:18px;border-radius:50%;background:var(--sky);display:block}
.socials i:nth-child(2){background:var(--grass)}
.socials i:nth-child(3){background:var(--pink)}
.socials i:nth-child(4){background:#f4c23e}
.contribute{left:718px;top:237px;width:112px;height:44px;background:var(--pink-pale);border:1px dashed var(--pink);border-radius:6px;padding:5px 6px}
.contribute .side-title{font-size:11px}
.contribute p{font-size:7px;color:var(--muted);margin-top:3px}
.sponsors{left:718px;top:293px;width:112px;height:154px;border:1px solid var(--line);border-radius:6px;padding:5px}
.sponsor-art{width:100px;height:116px;margin-top:4px;background:linear-gradient(180deg,#ffd6e4,#fff3c9)}
.popular{left:718px;top:460px;width:112px;background:var(--pink-pale);border-radius:6px;padding:6px 7px;height:223px}
.popular h4{font-family:"Lobster",cursive;font-weight:400;color:var(--pink);font-size:13px;line-height:1.15;margin-bottom:4px}
.popular li{list-style:none;font-size:7px;color:var(--text);padding:5px 0;border-bottom:1px dotted #eabccc}
.pop-grid{left:718px;top:697px;width:112px;display:grid;grid-template-columns:1fr 1fr;gap:6px 6px}
.pop-grid div{font-size:6.5px;color:var(--text);line-height:1.25}
.pop-grid b{display:block;height:50px;border-radius:3px;margin-bottom:2px;background:linear-gradient(180deg,#f7c5d6,#d48f9f)}
.pop-grid div:nth-child(2) b{background:linear-gradient(180deg,#fbe6c4,#c48a5b)}
.pop-grid div:nth-child(3) b{background:linear-gradient(180deg,#fde1ea,#e7a0b7)}
.pop-grid div:nth-child(4) b{background:linear-gradient(180deg,#e5d5f0,#a2789e)}
.like-box{left:718px;top:893px;width:112px;height:150px;border:1px solid #d9dde6}
.like-head{height:22px;background:#eef1f6;font-size:7.5px;font-weight:700;color:#4a5a78;padding:6px}
.like-faces{display:grid;grid-template-columns:repeat(4,1fr);gap:4px;padding:6px}
.like-faces i{display:block;height:20px;background:#dfe3ea}

/* footer */
.footer-nav{left:0;top:1122px;width:837px;display:flex;justify-content:center;gap:14px;font-size:7px;font-weight:700;color:#555}
.copyright{left:0;top:1136px;width:837px;text-align:center;font-size:6.5px;color:var(--muted)}
.footer-scene{left:0;top:1155px;width:837px;height:45px;background:linear-gradient(180deg,#c9e8a6,var(--grass) 55%,var(--grass-dark))}
</style>
</head>
<body>

<div class="abs header-scene" role="img" aria-label="Illustrated cupcake garden: sky, clouds, sun, green hills and grass dotted with cupcakes"></div>
<div class="abs site-title">Muffin Meadow</div>
<div class="abs site-tagline">Best cupcakes recipes all around the web featured at one place</div>
<nav class="abs main-nav">
  <a href="#">Home</a><a href="#">Cupcakes etc</a><a href="#">Muffin Meadow Recipes</a><a href="#">Contact</a>
  <span class="search">Search</span>
</nav>

<div class="abs cat-head">Featured Cupcakes<br>By Category</div>
<ul class="abs cat-list">
  <li><span class="cat-thumb" role="img" aria-label="Cupcake"></span><span>Cupcakes By Flavor</span><span>›</span></li>
  <li><span class="cat-thumb" role="img" aria-label="Cupcake"></span><span>Fruit cupcakes</span><span>›</span></li>
  <li><span class="cat-thumb" role="img" aria-label="Cupcake"></span><span>Holiday cupcakes</span><span>›</span></li>
  <li><span class="cat-thumb" role="img" aria-label="Cupcake"></span><span>Savory cupcakes</span><span>›</span></li>
  <li><span class="cat-thumb" role="img" aria-label="Cupcake"></span><span>Special cupcakes</span><span>›</span></li>
</ul>
<div class="abs ad-tall ad-red" role="img" aria-label="Vertical advertising banner"></div>
<div class="abs ad-tall ad-info" role="img" aria-label="Vertical advertising banner for infographic templates"></div>
<div class="abs badge-box">
  <h4>Grab Our Badge</h4>
  <div class="badge-art" role="img" aria-label="Blog badge with cupcake illustration"></div>
</div>
<div class="abs code-box">&lt;a href="muffinmeadow.net"&gt;&lt;img src="badge" /&gt;&lt;/a&gt;</div>

<article class="abs post" style="top:198px">
  <div class="post-thumb" role="img" aria-label="Cupcake photo"></div>
  <h2 class="post-title">Grasshopper Cupcakes by The Sweet Neighbors of Riverton</h2>
  <p class="post-meta">Posted by admin &nbsp;|&nbsp; April 2, 2014<br>Category: mint cupcakes</p>
  <p class="post-excerpt">Chocolate cake topped with a creamy mint frosting and a drizzle of dark ganache. A fresh and simple treat for any spring party or family gathering at home.</p>
  <span class="read-more">Read more</span>
</article>
<article class="abs post" style="top:370px">
  <div class="post-thumb" role="img" aria-label="Cupcake photo"></div>
  <h2 class="post-title">Grasshopper Cupcakes by The Sweet Neighbors of Riverton</h2>
  <p class="post-meta">Posted by admin &nbsp;|&nbsp; April 2, 2014<br>Category: mint cupcakes</p>
  <p class="post-excerpt">Chocolate cake topped with a creamy mint frosting and a drizzle of dark ganache. A fresh and simple treat for any spring party or family gathering at home.</p>
  <span class="read-more">Read more</span>
</article>
<article class="abs post" style="top:542px">
  <div class="post-thumb" role="img" aria-label="Cupcake photo"></div>
  <h2 class="post-title">Grasshopper Cupcakes by The Sweet Neighbors of Riverton</h2>
  <p class="post-meta">Posted by admin &nbsp;|&nbsp; April 2, 2014<br>Category: mint cupcakes</p>
  <p class="post-excerpt">Chocolate cake topped with a creamy mint frosting and a drizzle of dark ganache. A fresh and simple treat for any spring party or family gathering at home.</p>
  <span class="read-more">Read more</span>
</article>
<article class="abs post" style="top:714px">
  <div class="post-thumb" role="img" aria-label="Cupcake photo"></div>
  <h2 class="post-title">Grasshopper Cupcakes by The Sweet Neighbors of Riverton</h2>
  <p class="post-meta">Posted by admin &nbsp;|&nbsp; April 2, 2014<br>Category: mint cupcakes</p>
  <p class="post-excerpt">Chocolate cake topped with a creamy mint frosting and a drizzle of dark ganache. A fresh and simple treat for any spring party or family gathering at home.</p>
  <span class="read-more">Read more</span>
</article>
<article class="abs post" style="top:886px">
  <div class="post-thumb" role="img" aria-label="Cupcake photo"></div>
  <h2 class="post-title">Grasshopper Cupcakes by The Sweet Neighbors of Riverton</h2>
  <p class="post-meta">Posted by admin &nbsp;|&nbsp; April 2, 2014<br>Category: mint cupcakes</p>
  <p class="post-excerpt">Chocolate cake topped with a creamy mint frosting and a drizzle of dark ganache. A fresh and simple treat for any spring party or family gathering at home.</p>
  <span class="read-more">Read more</span>
</article>

<div class="abs pagination"><span>‹</span><span class="on">1</span><span>2</span><span>3</span><span>4</span><span>5</span><span>›</span></div>

<div class="abs follow">
  <div class="side-title">Follow Us</div>
  <div class="socials"><i></i><i></i><i></i><i></i><i></i></div>
</div>
<div class="abs contribute">
  <div class="side-title">Contribute to Our Site</div>
  <p>Share your favorite recipe</p>
</div>
<div class="abs sponsors">
  <div class="side-title">Our Sponsors</div>
  <div class="sponsor-art" role="img" aria-label="Sponsor banner"></div>
</div>
<div class="abs popular">
  <h4>Most Popular<br>Cupcakes</h4>
  <ul>
    <li>Cookie Dough Cupcakes with Brown Butter Frosting</li>
    <li>Coconut Banana Peanut Butter Cup Cupcakes</li>
    <li>Caramel Apple White Wine Cupcakes</li>
    <li>Fudgy Brownie Cupcakes</li>
    <li>Blackberry Cupcakes</li>
  </ul>
</div>
<div class="abs pop-grid">
  <div><b role="img" aria-label="Cupcake photo"></b>Berry Cream Cupcakes</div>
  <div><b role="img" aria-label="Cupcake photo"></b>Salted Toffee Cupcakes</div>
  <div><b role="img" aria-label="Cupcake photo"></b>Vanilla Rose Cupcakes</div>
  <div><b role="img" aria-label="Cupcake photo"></b>Plum Spice Cupcakes</div>
</div>
<div class="abs like-box">
  <div class="like-head">Muffin Meadow</div>
  <div class="like-faces"><i></i><i></i><i></i><i></i><i></i><i></i><i></i><i></i></div>
</div>

<nav class="abs footer-nav"><span>HOME</span><span>CUPCAKES ETC</span><span>MUFFIN MEADOW RECIPES</span><span>CONTACT</span></nav>
<div class="abs copyright">Copyright © 2014 muffinmeadow.net</div>
<div class="abs footer-scene" role="img" aria-label="Grass strip with flowers, cupcakes and a little girl illustration"></div>

</body>
</html>
```